KMR Business cards

I currently have a logo that was designed by a pixel harbor designer. I would like this to be added to the business card.

We are an innovative new start-up business offering finance solutions to the car dealership market in the UK. So our clients are quiet traditional, so are cards need to fit in, but at the same time show we are a modern online business.

Finance

```html
<!DOCTYPE html>
<html lang="en">
<head>
<meta charset="utf-8">
<title>KMR Business Card</title>
<link href="https://fonts.googleapis.com/css2?family=Lato:wght@400;700;900&display=swap" rel="stylesheet">
<style>
  :root {
    --paper: #ffffff;
    --mist-light: #f4fbfb;
    --mist: #d9efee;
    --teal-soft: #b9dcd9;
    --navy: #18206b;
    --panel-light: #56646c;
    --panel-mid: #2f3b45;
    --panel-dark: #171f29;
    --text-light: #ffffff;
    --rule: rgba(255,255,255,0.35);
    --icon: #0d0f12;
    --strip-top: #9ab6c0;
    --strip-bottom: #4e6c86;
  }
  * { margin: 0; padding: 0; box-sizing: border-box; }
  html, body { width: 1200px; height: 720px; overflow: hidden; background: var(--paper); }
  body { font-family: "Lato", sans-serif; }
  .card { position: relative; width: 1200px; height: 720px; background: var(--paper); }

  .brand-band {
    position: absolute; left: 0; top: 6px; width: 1200px; height: 276px;
    background: linear-gradient(90deg, var(--mist) 0%, var(--mist-light) 55%, var(--paper) 100%);
  }
  .hero-art {
    position: absolute; left: 0; top: 0; width: 590px; height: 276px;
    background: radial-gradient(ellipse at 55% 60%, var(--teal-soft) 0%, var(--mist) 55%, rgba(217,239,238,0) 100%);
  }
  .brand-mark {
    position: absolute; left: 578px; top: 30px; height: 220px;
    display: flex; align-items: center; gap: 28px;
  }
  .brand-ring {
    width: 200px; height: 200px; border-radius: 50%;
    border: 10px solid var(--navy); flex-shrink: 0;
  }
  .brand-name {
    color: var(--navy); font-weight: 400; font-size: 54px; line-height: 1.08;
  }

  .contact-panel {
    position: absolute; left: 0; top: 288px; width: 1200px; height: 376px;
    background:
      radial-gradient(ellipse 60% 45% at 50% 10%, var(--panel-light) 0%, rgba(86,100,108,0) 100%),
      linear-gradient(180deg, var(--panel-mid) 0%, var(--panel-dark) 100%);
  }
  .contact-list { list-style: none; position: absolute; left: 44px; top: 52px; }
  .contact-item { display: flex; align-items: center; height: 72px; }
  .contact-item:nth-child(3) { margin-top: 8px; }
  .contact-icon { width: 46px; height: 46px; display: flex; justify-content: center; align-items: center; margin-right: 26px; }
  .contact-text {
    color: var(--text-light); font-size: 27px; letter-spacing: 0.5px;
    padding: 6px 16px 8px 0;
    border-bottom: 1px solid var(--rule);
    border-image: linear-gradient(90deg, rgba(255,255,255,0.05), var(--rule) 20%, var(--rule) 80%, rgba(255,255,255,0)) 1;
  }

  .person { position: absolute; left: 600px; top: 82px; width: 520px; text-align: center; color: var(--text-light); }
  .person-name { font-size: 50px; line-height: 1; text-shadow: 0 0 8px rgba(255,255,255,0.35); }
  .person-name .given { font-weight: 900; }
  .person-name .family { font-weight: 400; }
  .person-role { font-size: 41px; font-weight: 400; margin-top: 4px; }

  .footer-strip {
    position: absolute; left: 2px; top: 680px; width: 1196px; height: 40px;
    background: linear-gradient(180deg, var(--strip-top) 0%, var(--strip-bottom) 100%);
  }
</style>
</head>
<body>
<div class="card">
  <header class="brand-band">
    <div class="hero-art" role="img" aria-label="Illustration of business people in silhouette standing before a faint sports car"></div>
    <div class="brand-mark">
      <div class="brand-ring"></div>
      <div class="brand-name">Kingsmere<br>Motor<br>Resources</div>
    </div>
  </header>

  <section class="contact-panel">
    <ul class="contact-list">
      <li class="contact-item">
        <span class="contact-icon">
          <svg width="28" height="50" viewBox="0 0 28 50"><rect x="1" y="1" width="26" height="48" rx="5" fill="var(--icon)"/><rect x="4" y="8" width="20" height="32" fill="#3a434c"/><circle cx="14" cy="44" r="2.5" fill="#3a434c"/></svg>
        </span>
        <span class="contact-text">07700 900418</span>
      </li>
      <li class="contact-item">
        <span class="contact-icon">
          <svg width="44" height="44" viewBox="0 0 44 44"><circle cx="22" cy="22" r="21" fill="var(--icon)"/></svg>
        </span>
        <span class="contact-text">daniel.harper_kmr</span>
      </li>
      <li class="contact-item">
        <span class="contact-icon">
          <svg width="46" height="46" viewBox="0 0 46 46" fill="none" stroke="var(--icon)" stroke-width="3"><circle cx="23" cy="23" r="20"/><ellipse cx="23" cy="23" rx="9" ry="20"/><line x1="3" y1="23" x2="43" y2="23"/><path d="M7 12h32M7 34h32"/></svg>
        </span>
        <span class="contact-text">www.kingsmeremotor.com</span>
      </li>
      <li class="contact-item">
        <span class="contact-icon">
          <svg width="44" height="36" viewBox="0 0 44 36" fill="none" stroke="var(--icon)" stroke-width="3.5"><rect x="2" y="2" width="40" height="32"/><path d="M2 2l20 18 20-18M2 34l15-14M42 34L27 20"/></svg>
        </span>
        <span class="contact-text">daniel.harper@kingsmeremotor.com</span>
      </li>
    </ul>

    <div class="person">
      <h1 class="person-name"><span class="given">DANIEL</span> <span class="family">HARPER</span></h1>
      <p class="person-role">Founder</p>
    </div>
  </section>

  <footer class="footer-strip"></footer>
</div>
</body>
</html>
```